Now Leasing Banner

Looking for a banner that says the following information approx 4' x 30'

Now Leasing Maplewood Terrace 925-318-6054

Target Market(s)

Drive by traffic

Industry/Entity Type

Residential property management

Requirements
Must have
• Clear and readable from a distance

```html
<!DOCTYPE html>
<html lang="en">
<head>
<meta charset="utf-8">
<title>Now Leasing Banner – Maplewood Terrace</title>
<link href="https://fonts.googleapis.com/css2?family=Montserrat:wght@700;800&display=swap" rel="stylesheet">
<style>
  :root {
    --backdrop: #d4d5d6;
    --leasing-blue: #4569b2;
    --banner-white: #ffffff;
    --brand-green: #27b799;
  }
  html, body {
    margin: 0;
    padding: 0;
    width: 1200px;
    height: 1200px;
    overflow: hidden;
    background: var(--backdrop);
  }
  .canvas {
    width: 1200px;
    height: 1200px;
    display: flex;
    align-items: center;
    justify-content: center;
  }
  .banner {
    width: 222px;
    height: 1150px;
    display: flex;
    flex-direction: column;
    background: var(--banner-white);
    overflow: hidden;
  }
  .banner__message {
    display: flex;
    height: 926px;
  }
  .banner__headline {
    width: 128px;
    background: var(--leasing-blue);
    color: var(--banner-white);
  }
  .banner__phone {
    flex: 1;
    background: var(--banner-white);
    color: var(--leasing-blue);
  }
  .stacked-text {
    margin: 0;
    padding-top: 46px;
    display: flex;
    flex-direction: column;
    align-items: center;
    font-family: "Montserrat", sans-serif;
    font-weight: 800;
    font-size: 50px;
    line-height: 70px;
  }
  .stacked-text__char,
  .stacked-text__gap {
    display: block;
    height: 70px;
  }
  .banner__brand {
    flex: 1;
    background: var(--brand-green);
    display: flex;
    align-items: center;
    justify-content: center;
  }
  .brand-name {
    margin: 0;
    font-family: "Montserrat", sans-serif;
    font-weight: 800;
    font-size: 31px;
    line-height: 1.2;
    color: var(--banner-white);
    text-align: center;
  }
</style>
</head>
<body>
  <main class="canvas">
    <section class="banner" aria-label="Now Leasing banner">
      <div class="banner__message">
        <div class="banner__headline">
          <h1 class="stacked-text" aria-label="Now Leasing">
            <span class="stacked-text__char">N</span>
            <span class="stacked-text__char">O</span>
            <span class="stacked-text__char">W</span>
            <span class="stacked-text__gap"></span>
            <span class="stacked-text__char">L</span>
            <span class="stacked-text__char">E</span>
            <span class="stacked-text__char">A</span>
            <span class="stacked-text__char">S</span>
            <span class="stacked-text__char">I</span>
            <span class="stacked-text__char">N</span>
            <span class="stacked-text__char">G</span>
          </h1>
        </div>
        <div class="banner__phone">
          <p class="stacked-text" aria-label="925-318-6054">
            <span class="stacked-text__char">9</span>
            <span class="stacked-text__char">2</span>
            <span class="stacked-text__char">5</span>
            <span class="stacked-text__gap"></span>
            <span class="stacked-text__char">3</span>
            <span class="stacked-text__char">1</span>
            <span class="stacked-text__char">8</span>
            <span class="stacked-text__gap"></span>
            <span class="stacked-text__char">6</span>
            <span class="stacked-text__char">0</span>
            <span class="stacked-text__char">5</span>
            <span class="stacked-text__char">4</span>
          </p>
        </div>
      </div>
      <div class="banner__brand">
        <p class="brand-name">Maplewood<br>Terrace</p>
      </div>
    </section>
  </main>
</body>
</html>
```